Cosmetics Brand Logo and Bottle Label Design

We are creating a new cosmetics brand called "Nolan Whitby" and would like you to create an amazing logo and bottle label for this brand's new 100% pure argan oil product.
For the logo, we really like the logo's of Marin Calloway and Vessa. The text should be Sans Serif (without feet).
For the actual bottle label, please find attached labels of one of our competitors design which really like. We really like the simplicity and elegance of the design. The only difference is that our product will be using light turqoise as the brand color. Please feel free to add your own creativity into it as well.
Industry/Entity Type
Cosmetics
Logo Text
Nolan Whitby
Font styles to use

```html
<!DOCTYPE html>
<html lang="en">
<head>
<meta charset="utf-8">
<title>Nolan Whitby Argan Oil – Label Concepts</title>
<link rel="stylesheet" href="https://fonts.googleapis.com/css2?family=Barlow:wght@300;400;500&display=swap">
<style>
  :root {
    --paper: #ffffff;
    --canvas: #fbfbfb;
    --ink: #1f1f1f;
    --ink-soft: #555555;
    --teal: #1cbfa6;
    --mint: #7fdccc;
    --label-shadow: rgba(0,0,0,0.08);
  }
  html, body {
    margin: 0;
    padding: 0;
    width: 1191px;
    height: 1200px;
    overflow: hidden;
    background: var(--canvas);
    font-family: "Barlow", sans-serif;
  }
  .board {
    position: relative;
    width: 1191px;
    height: 1200px;
  }
  .label {
    position: absolute;
    width: 150px;
    height: 188px;
    background: var(--paper);
    box-shadow: 0 1px 4px var(--label-shadow), inset 0 0 0 1px #eeeeee;
    overflow: hidden;
    color: var(--ink);
    text-transform: uppercase;
    font-weight: 400;
  }
  .row-top .label { top: 262px; }
  .row-bottom .label { top: 824px; }

  .center-stack {
    position: absolute;
    left: 0; right: 0;
    text-align: center;
  }
  .brand-teal { color: var(--teal); }
  .small { font-size: 7px; letter-spacing: 0.06em; color: var(--ink-soft); }

  /* 1 – centred classic */
  .label--classic .center-stack { top: 77px; }
  .label--classic .brand { font-size: 11px; letter-spacing: 0.08em; }
  .label--classic .product { font-size: 10.5px; letter-spacing: 0.08em; margin-top: 4px; }
  .label--classic .small { margin-top: 3px; }

  /* 2 – oversized type */
  .label--bold .headline {
    position: absolute; left: 14px; top: 20px;
    font-weight: 300; font-size: 52px; line-height: 46px; letter-spacing: 0.04em;
  }
  .label--bold .brand {
    position: absolute; left: 95px; top: 22px;
    font-size: 10px; line-height: 13px; letter-spacing: 0.04em; font-weight: 300;
  }
  .label--bold .small { position: absolute; left: 60px; top: 168px; }

  /* 3 – offset block */
  .label--offset .block {
    position: absolute; left: 74px; top: 34px;
    border-left: 1px solid var(--teal); padding-left: 5px;
  }
  .label--offset .brand { font-size: 10px; line-height: 14px; font-weight: 300; letter-spacing: 0.04em; }
  .label--offset .product { font-size: 10px; letter-spacing: 0.1em; margin-top: 3px; padding-left: 0; }
  .label--offset .small { margin-top: 2px; }

  /* 4 – vertical type */
  .label--vertical .rule {
    position: absolute; left: 0; right: 0; top: 0; height: 3px; background: var(--teal);
  }
  .label--vertical .rotated {
    position: absolute; left: 40px; top: 145px;
    transform: rotate(-90deg); transform-origin: left top;
    white-space: nowrap;
  }
  .label--vertical .brand { font-size: 24px; line-height: 24px; font-weight: 300; letter-spacing: 0.03em; }
  .label--vertical .product { font-size: 10px; letter-spacing: 0.1em; margin-top: 4px; }
  .label--vertical .small { font-size: 6px; }

  /* 5 – mint gradient */
  .label--gradient {
    background: linear-gradient(180deg, var(--mint) 0%, #a8e8dc 40%, var(--paper) 78%);
  }
  .label--gradient .center-stack { top: 22px; color: var(--paper); }
  .label--gradient .brand-top { font-size: 13px; letter-spacing: 0.06em; font-weight: 300; }
  .label--gradient .brand-main { font-size: 22px; font-weight: 300; line-height: 24px; letter-spacing: -0.01em; }
  .label--gradient .product { font-size: 9px; letter-spacing: 0.12em; margin-top: 4px; }
  .label--gradient .small { position: absolute; left: 0; right: 0; top: 168px; text-align: center; }

  /* 6 – teal tab */
  .label--tab .tab {
    position: absolute; left: 47px; right: 0; top: 46px; height: 30px;
    background: var(--teal); color: var(--paper);
    font-size: 11px; line-height: 30px; text-align: center; letter-spacing: 0.02em;
  }
  .label--tab .product {
    position: absolute; left: 50px; top: 84px;
    font-size: 15px; letter-spacing: 0.06em; font-weight: 400;
  }

  /* 7 – big Oil */
  .label--oil .center-stack { top: 37px; }
  .label--oil .eyebrow { font-size: 17px; letter-spacing: 0.04em; color: var(--teal); font-weight: 300; }
  .label--oil .big {
    font-size: 70px; line-height: 52px; font-weight: 500; color: var(--teal);
    text-transform: none; letter-spacing: -0.02em; margin-top: 2px;
  }
  .label--oil .brand { font-size: 10px; letter-spacing: 0.06em; margin-top: 10px; }
  .label--oil .small { font-size: 9px; margin-top: 23px; color: var(--ink); }

  /* 8 – stacked name */
  .label--stacked .center-stack { top: 14px; }
  .label--stacked .brand-main { font-size: 22px; font-weight: 300; line-height: 24px; color: var(--teal); letter-spacing: 0.02em; }
  .label--stacked .product { font-size: 16px; letter-spacing: 0.08em; margin-top: 32px; font-weight: 300; }
  .label--stacked .small { font-size: 10px; margin-top: 2px; color: var(--ink); }

  /* 9 – dashed wordmark */
  .label--wordmark .center-stack { top: 44px; }
  .label--wordmark .brand-top { font-size: 19px; letter-spacing: 0.06em; font-weight: 300; color: var(--teal); }
  .label--wordmark .brand-main { font-size: 30px; line-height: 34px; font-weight: 300; color: var(--teal); letter-spacing: -0.01em; }
  .label--wordmark .product { font-size: 14px; letter-spacing: 0.08em; margin-top: 4px; }
  .label--wordmark .small { font-size: 9.5px; color: var(--ink); margin-top: 1px; }
</style>
</head>
<body>
<main class="board">
  <section class="row-top">
    <article class="label label--classic" style="left:121px">
      <div class="center-stack">
        <div class="brand brand-teal">– Nolan Whitby –</div>
        <div class="product">Argan Oil</div>
        <div class="small">100% Pure</div>
      </div>
    </article>

    <article class="label label--bold" style="left:327px">
      <div class="headline">Ar<br>Gan<br>Oil</div>
      <div class="brand brand-teal">Nolan<br>Whitby</div>
      <div class="small">100% Pure</div>
    </article>

    <article class="label label--offset" style="left:538px">
      <div class="block">
        <div class="brand brand-teal">Nolan<br>Whitby</div>
        <div class="product">Argan Oil</div>
        <div class="small">100% Pure</div>
      </div>
    </article>

    <article class="label label--vertical" style="left:722px">
      <div class="rule"></div>
      <div class="rotated">
        <div class="brand brand-teal">Nolan<br>Whitby</div>
        <div class="product">Argan Oil</div>
        <div class="small">100% Pure</div>
      </div>
    </article>

    <article class="label label--gradient" style="left:896px">
      <div class="center-stack">
        <div class="brand-top">– Nolan –</div>
        <div class="brand-main">WHITBY</div>
        <div class="product">Argan Oil</div>
      </div>
      <div class="small">100% Pure</div>
    </article>
  </section>

  <section class="row-bottom">
    <article class="label label--tab" style="left:115px">
      <div class="tab">Nolan Whitby</div>
      <div class="product">Argan Oil</div>
    </article>

    <article class="label label--oil" style="left:310px">
      <div class="center-stack">
        <div class="eyebrow">Argan</div>
        <div class="big">Oil</div>
        <div class="brand">– Nolan Whitby –</div>
        <div class="small">100% Pure</div>
      </div>
    </article>

    <article class="label label--stacked" style="left:497px">
      <div class="center-stack">
        <div class="brand-main">Nolan<br>Whitby</div>
        <div class="product">Argan Oil</div>
        <div class="small">100% Pure</div>
      </div>
    </article>

    <article class="label label--wordmark" style="left:702px">
      <div class="center-stack">
        <div class="brand-top">– Nolan –</div>
        <div class="brand-main">WHITBY</div>
        <div class="product">Argan Oil</div>
        <div class="small">100% Pure</div>
      </div>
    </article>
  </section>
</main>
</body>
</html>
```